Professional Music Editor Needs a Book Cover Design

I need a book cover design for a series of books which will include excerpts from symphonic pieces required for auditions in professional symphony orchestras. The books will contain text and a lot of music examples. The book will be published in a Brivo and eLeafs version, to be used mainly on an zTab, but will be also available in print in A4 size. The cover may incorporate notation or/and violin images.

The text on the cover should include:

Author: Teodor Markelin D.M.A.
Series: Morning Scales Concert Passages for Violin
Title: Anselm Berlicke, Pale Tower Op. 20, measures 1-62
Updates

Thank you so much for the submitted projects so far! I have uploaded one more photo, which I think may be a good element to use. If you decide to incorporate it, please use just the violin from the photo, not the person. 

And one more thing: I would like the design to be modern, rather than traditional.

Thanks a lot for your work!

Target Market(s)

The target customers of this edition are college students who are going to use the book to prepare for auditions for professional orchestras.

Industry/Entity Type

It Professional

Colors
ffffff

```html
<!DOCTYPE html>
<html lang="en">
<head>
<meta charset="utf-8">
<title>Morning Scales Concert Passages for Violin — Book Cover</title>
<link rel="stylesheet" href="https://fonts.googleapis.com/css2?family=Questrial&family=Mulish:wght@600;800&display=swap">
<style>
  :root {
    --page-bg: #ffffff;
    --cover-grey: #c9cacc;
    --cover-glow: #f4f4f5;
    --title-white: #ffffff;
    --band-rust: #a24f38;
    --band-edge: #d8a07c;
    --band-text: #fbeee6;
    --author-rust: #a24f38;
    --violin-dark: #6a2f14;
    --violin-mid: #b7652c;
    --violin-light: #d98a45;
  }
  * { margin: 0; padding: 0; box-sizing: border-box; }
  html, body {
    width: 1200px;
    height: 900px;
    overflow: hidden;
    background: var(--page-bg);
  }
  .canvas {
    position: relative;
    width: 1200px;
    height: 900px;
    background: var(--page-bg);
  }
  .book-cover {
    position: absolute;
    left: 361px;
    top: 112px;
    width: 477px;
    height: 676px;
    background: radial-gradient(ellipse 230px 300px at 50% 62%, var(--cover-glow) 0%, #e3e4e5 45%, var(--cover-grey) 100%);
    overflow: hidden;
  }
  .series-title {
    position: absolute;
    left: 31px;
    top: 34px;
    width: 430px;
    font-family: "Mulish", sans-serif;
    font-weight: 600;
    font-size: 33px;
    line-height: 34px;
    letter-spacing: 0.3px;
    color: var(--title-white);
    text-transform: uppercase;
  }
  .title-band {
    position: absolute;
    left: 22px;
    top: 153px;
    width: 432px;
    height: 28px;
    background: var(--band-rust);
    border: 2px solid var(--band-edge);
    display: flex;
    align-items: center;
    justify-content: center;
    font-family: "Questrial", sans-serif;
    font-size: 14.5px;
    color: var(--band-text);
    text-transform: uppercase;
    white-space: nowrap;
  }
  .violin-photo {
    position: absolute;
    left: 170px;
    top: 206px;
    width: 140px;
    height: 350px;
  }
  .author {
    position: absolute;
    left: 0;
    right: 0;
    top: 600px;
    text-align: center;
    font-family: "Mulish", sans-serif;
    font-weight: 800;
    font-size: 16px;
    letter-spacing: -0.2px;
    color: var(--author-rust);
    text-transform: uppercase;
  }
</style>
</head>
<body>
  <main class="canvas">
    <section class="book-cover">
      <h1 class="series-title">Morning Scales<br>Concert Passages<br>for Violin</h1>
      <p class="title-band">Anselm Berlicke, Pale Tower Op. 20, Measures 1 - 62</p>
      <svg class="violin-photo" viewBox="0 0 140 350" role="img" aria-label="Photograph of a violin standing upright, scroll at top, casting a soft shadow">
        <defs>
          <linearGradient id="violin-wood" x1="0" y1="0" x2="1" y2="1">
            <stop offset="0" stop-color="var(--violin-light)"/>
            <stop offset="0.55" stop-color="var(--violin-mid)"/>
            <stop offset="1" stop-color="var(--violin-dark)"/>
          </linearGradient>
        </defs>
        <rect x="0" y="0" width="140" height="350" rx="60" fill="url(#violin-wood)" opacity="0.85"/>
      </svg>
      <p class="author">Teodor Markelin D.M.A.</p>
    </section>
  </main>
</body>
</html>
```